Out Door Living brochure

We need a Great looking brochure to feature the latest in out door living. Showcasing out doors is the new living space.

I'm enclosing our logo and a brochure we had done recently it didn't have enough impact. This one was a single fold you can also provide a tri fold if you see fit. We like the verbiage, but if you can spice it up we would love to see that. This brochure will be added to our sales packet.
Thank you!!!

Target Market(s)

Home owners

Industry/Entity Type

Construction Company

Logo Text

(See logo) Beautiful Homes Built to Last Introducing Outdoor living 2017

Font styles to use
Serif

Requirements
Must have
• Logo and
• Beautiful Homes Built to Last
• Introducing Outdoor living 2017
Nice to have
• Benefits of outdoor living
Should not have
• Bad photos if these don't work let me know we can get others to replace the sapce

```html
<!DOCTYPE html>
<html lang="en">
<head>
<meta charset="utf-8">
<title>Harbor Ridge Builders — Outdoor Living Brochure</title>
<link href="https://fonts.googleapis.com/css2?family=Montserrat:wght@400;500&family=Roboto:wght@400&display=swap" rel="stylesheet">
<style>
  :root {
    --backdrop: #5e5e5f;
    --sky: #82c0ea;
    --sky-deep: #5b9fcf;
    --steel: #7a7d84;
    --paper: #ffffff;
    --paper-shade: #dcdddf;
    --ink-grey: #707278;
    --wood: #8a7664;
    --stone: #9a9a98;
  }
  * { margin: 0; padding: 0; box-sizing: border-box; }
  html, body { width: 1200px; height: 1200px; overflow: hidden; }
  body {
    background: var(--backdrop);
    font-family: "Montserrat", sans-serif;
    position: relative;
  }
  .page {
    position: absolute;
    top: 230px;
    width: 520px;
    height: 740px;
    box-shadow: 0 6px 18px rgba(0,0,0,0.35);
    overflow: hidden;
  }
  .back-cover {
    left: 60px;
    background: linear-gradient(135deg, var(--sky) 0%, #75b5e2 50%, var(--sky-deep) 100%);
  }
  .contact {
    position: absolute;
    left: 34px;
    bottom: 40px;
    color: var(--paper);
    list-style: none;
    font-size: 13px;
    line-height: 1.7;
  }
  .contact .address { font-size: 12.5px; margin-bottom: 2px; }
  .contact .phone { font-size: 19px; font-weight: 500; }
  .contact li { display: flex; align-items: center; gap: 9px; }
  .contact svg { width: 13px; height: 13px; flex: none; }
  .front-cover { left: 620px; background: var(--paper); }
  .front-art { position: absolute; inset: 0; }
  .brand {
    position: absolute;
    left: 44px;
    top: 70px;
    display: flex;
    align-items: center;
    gap: 10px;
    color: var(--ink-grey);
    font-size: 15px;
    font-weight: 400;
    letter-spacing: 0.5px;
  }
  .brand-square { width: 22px; height: 22px; background: var(--sky-deep); }
  .tagline {
    position: absolute;
    left: 200px;
    top: 630px;
    color: var(--paper);
    font-family: "Roboto", sans-serif;
    font-size: 20px;
    line-height: 1.3;
  }
</style>
</head>
<body>
  <section class="page back-cover" aria-label="Back cover">
    <ul class="contact">
      <li class="address">1480 Alder Crest Ave., Bayview, CA 94010</li>
      <li class="phone">
        <svg viewBox="0 0 16 16" aria-hidden="true"><path fill="#fff" d="M3 1h3l1 4-2 1a9 9 0 0 0 5 5l1-2 4 1v3c0 1-1 2-2 2A13 13 0 0 1 1 3c0-1 1-2 2-2z"/></svg>
        (555)-014-2296
      </li>
      <li>
        <svg viewBox="0 0 16 16" aria-hidden="true"><rect x="1" y="3" width="14" height="10" fill="#fff"/><path d="M1 3l7 6 7-6" fill="none" stroke="#6aaede" stroke-width="1.4"/></svg>
        hello@harborridgemail.net
      </li>
      <li>
        <svg viewBox="0 0 16 16" aria-hidden="true"><circle cx="8" cy="8" r="7" fill="#fff"/><path d="M1 8h14M8 1c-3 4-3 10 0 14M8 1c3 4 3 10 0 14" fill="none" stroke="#6aaede" stroke-width="1"/></svg>
        www.harborridgebuilders.com
      </li>
    </ul>
  </section>

  <section class="page front-cover" aria-label="Front cover">
    <svg class="front-art" viewBox="0 0 520 740" aria-hidden="false">
      <defs>
        <linearGradient id="paperFade" x1="0" y1="0" x2="1" y2="1">
          <stop offset="0" stop-color="#f4f4f5"/>
          <stop offset="0.5" stop-color="#ffffff"/>
          <stop offset="1" stop-color="#d8d9db"/>
        </linearGradient>
        <linearGradient id="blueFade" x1="0" y1="0" x2="1" y2="1">
          <stop offset="0" stop-color="#6eaedd"/>
          <stop offset="0.5" stop-color="#86c3ec"/>
          <stop offset="1" stop-color="#5a9dcd"/>
        </linearGradient>
        <linearGradient id="photoTones" x1="0" y1="0" x2="1" y2="1">
          <stop offset="0" stop-color="#8a7664"/>
          <stop offset="0.45" stop-color="#7c7b78"/>
          <stop offset="0.75" stop-color="#9aa4a6"/>
          <stop offset="1" stop-color="#7fb4c0"/>
        </linearGradient>
      </defs>
      <rect width="520" height="740" fill="url(#paperFade)"/>
      <path d="M0 300 C40 560 200 610 520 500 L520 740 L0 740 Z" fill="url(#blueFade)"/>
      <path d="M120 330 C150 560 340 610 540 520" fill="none" stroke="#fff" stroke-width="10"/>
      <path d="M118 330 C148 548 340 598 540 508" fill="none" stroke="#7a7d84" stroke-width="9"/>
      <ellipse cx="385" cy="340" rx="270" ry="215" fill="#6ba9d8"/>
      <ellipse cx="392" cy="336" rx="256" ry="200" fill="url(#photoTones)"
               role="img" aria-label="Photo of a covered outdoor kitchen with grill, stone bar counter and pale blue bar stools"/>
    </svg>
    <div class="brand">
      <span class="brand-square" aria-hidden="true"></span>
      <span>HARBOR RIDGE BUILDERS</span>
    </div>
    <p class="tagline">Beautiful Homes Built to Last<br>Introducing Outdoor living 2017</p>
  </section>
</body>
</html>
```